Norwegian Mobile Home/Cabin Producer Needs Brochure Design

We make and deliver our own brand of mobile homes especially made for Norway and it's weather conditions. We differ from other brands in building quality in regards to a much more solid construction, insulation and choices. We work with our customer from the beginning and build them after their demands and wishes.
We need a brochure that holds us out as top of the line. We deliver mobile homes of all kinds and sizes. Both to the private and professional sector.
For the professional sector, mainly camping sites we want to show, lodges-, sanitary- and kitchen wagoons etc.
So we need a brochure of 14-20 pages in A4 where the double pages can be printed in A3 format.
We have logo (provided). But we need cover as well as back suggestions.
It should start with pages where we can teel who we are and stand for.Piicture(s) and space for some editable text (which we can write in norwegian). The text part can have a transparent background......or not. Give us your best shot. Also a smaller part in the private sector that shows winter time.
We want other pages for the private sector that shows what we deliver and the possibilities of choices.
Pages for the the professional sector.
Pages that show our production. How we transport. And the split construction. Only pictures from this portfolio here. (see fotoskap portfolios)
Take a look at provided pictures and our website www.solvikhytta.no for inspiration.
Here's a FotoSkap link to Pictures to choose from. http://bildelagr.example/K4TQ9P
(Hope it Works, let me know if not)
Our company name in small letters "fjordgrønn hyttebygg" means directly translated "fjordgreen cabin builds".
Looking forward to your suggestions.
Target Market(s)
Private market for vacation mobile homes. Camping sites and similar
Industry/Entity Type
Insulation
Requirements
Must have
- Our logo on the front page. Simple but inviting and professional
Logo and address on the back.

```html
<!DOCTYPE html>
<html lang="no">
<head>
<meta charset="utf-8">
<title>Valgene er dine – brosjyreoppslag</title>
<link rel="stylesheet" href="https://fonts.googleapis.com/css2?family=Source+Sans+3:ital,wght@0,400;0,600;1,400&display=swap">
<style>
  :root {
    --page-white: #ffffff;
    --lavender-light: #eeebf2;
    --lavender-deep: #bdb5d1;
    --ink: #3f3f45;
    --ink-soft: #5d5b66;
    --stamp-line: #c9c3d6;
  }
  * { box-sizing: border-box; margin: 0; padding: 0; }
  html, body { width: 1200px; height: 806px; overflow: hidden; background: var(--page-white); }
  .spread {
    position: relative;
    width: 1200px;
    height: 806px;
    font-family: "Source Sans 3", "Frutiger", sans-serif;
    color: var(--ink);
    overflow: hidden;
  }
  .spread__shapes { position: absolute; inset: 0; }

  .page-title {
    position: absolute;
    left: 28px;
    top: 78px;
    font-size: 26px;
    font-weight: 400;
    letter-spacing: 0.2px;
    color: var(--ink);
  }

  .choice-grid {
    position: absolute;
    left: 28px;
    top: 138px;
    width: 426px;
    height: 366px;
    display: grid;
    grid-template-columns: 1fr 1fr;
    grid-template-rows: 1fr 1fr;
    gap: 9px 6px;
  }
  .choice-grid__photo { width: 100%; height: 100%; }
  .photo--dining   { background: linear-gradient(160deg, #e9e4dd 0%, #b9afa6 55%, #6f5f5a 100%); }
  .photo--winter   { background: linear-gradient(170deg, #e6e8ea 0%, #b4b2ac 50%, #8a6f5c 100%); }
  .photo--bathroom { background: linear-gradient(180deg, #f2f4f5 0%, #dfe6ea 60%, #8fb2cf 100%); }
  .photo--bedroom  { background: linear-gradient(165deg, #efe9e1 0%, #d4c7b8 55%, #b8a08f 100%); }

  .quality-seal {
    position: absolute;
    left: 367px;
    top: 459px;
    width: 134px;
    height: 134px;
    border: 3px solid var(--stamp-line);
    border-radius: 50%;
    opacity: 0.7;
  }

  .pull-quote {
    position: absolute;
    left: 28px;
    top: 638px;
    width: 384px;
    font-size: 13px;
    font-style: italic;
    line-height: 22px;
    text-align: center;
    color: var(--ink-soft);
  }

  .feature-photo { position: absolute; inset: 0; }

  .article {
    position: absolute;
    top: 592px;
    width: 250px;
    font-size: 9.4px;
    line-height: 13.2px;
    color: var(--ink-soft);
    text-align: justify;
  }
  .article--first { left: 656px; }
  .article--second { left: 924px; top: 613px; width: 248px; }
  .article h2 {
    font-size: 14.5px;
    font-weight: 400;
    color: var(--ink);
    margin-bottom: 6px;
    text-align: left;
  }
  .article p + h2 { margin-top: 14px; }
  .article p + p { margin-top: 13px; }
</style>
</head>
<body>
<main class="spread">
  <svg class="spread__shapes" viewBox="0 0 1200 806" width="1200" height="806" aria-hidden="true">
    <path d="M0,0 H509 C562,210 592,500 600,806 H0 Z" fill="var(--lavender-light)"/>
    <path d="M596,289 H1200 V806 H600 C600,620 600,450 596,289 Z" fill="var(--lavender-deep)"/>
    <path d="M596,0 H1200 V512 C1060,536 910,542 800,516 C690,488 616,402 596,289 Z" fill="var(--page-white)"/>
    <path d="M748,470 C812,548 900,580 1012,584 C900,590 800,560 748,470 Z" fill="var(--page-white)"/>
  </svg>

  <svg class="feature-photo" viewBox="0 0 1200 806" width="1200" height="806" role="img" aria-label="Fotografi av lys stue med veggmontert TV, grønne puffer, glassbord med lys og store vinduer mot hagen">
    <defs>
      <linearGradient id="livingRoomTones" x1="0" y1="0" x2="1" y2="1">
        <stop offset="0" stop-color="#e3e0dc"/>
        <stop offset="0.45" stop-color="#cfcac4"/>
        <stop offset="0.7" stop-color="#9db85a"/>
        <stop offset="1" stop-color="#4a4a4e"/>
      </linearGradient>
    </defs>
    <path d="M631,0 H1200 V466 C1060,492 905,500 800,472 C710,447 650,362 631,266 Z" fill="url(#livingRoomTones)"/>
  </svg>

  <h1 class="page-title">Valgene er dine</h1>

  <div class="choice-grid">
    <div class="choice-grid__photo photo--dining" role="img" aria-label="Fotografi av åpent kjøkken og spisestue"></div>
    <div class="choice-grid__photo photo--winter" role="img" aria-label="Fotografi av sofa med puter foran vindu med vinterlandskap"></div>
    <div class="choice-grid__photo photo--bathroom" role="img" aria-label="Fotografi av lyst bad med dusjkabinett"></div>
    <div class="choice-grid__photo photo--bedroom" role="img" aria-label="Fotografi av soverom med seng under vindu"></div>
  </div>

  <div class="quality-seal" aria-hidden="true"></div>

  <p class="pull-quote">We believe that quality in a service or product is not what we put<br>into it. It is what our customers gets out of it.”</p>

  <section class="article article--first">
    <h2>Alia Doming Eirmod Eum</h2>
    <p>Movet dolore reprimique ea nec, sea no omnes tantas complectitur. Tale munere salutatus et his, utinam melius tibique nam et. His ut brute illud. Alia doming eirmod eum ei, tollit molestiae vel et. An cibo clita iisque qui, phaedrum moderatius no quo.</p>
    <h2>Ex Inani Argumentum</h2>
    <p>Movet dolore reprimique ea nec, sea no omnes tantas complectitur. Tale munere salutatus et his, utinam melius tibique nam et. His ut brute illud. Alia doming eirmod eu ex inani argumentum appellantur nam, noster graeco vel ei.</p>
  </section>

  <section class="article article--second">
    <p>et quod agam posse per. Has cu quot fastidii dissentiet. Ei cum duis fastidii. Et nam voluptua appetere, cu eos graeco facilis philosophia. Mei appetere forensibus at, timeam facilisis eu quo. Ei cum duis fastidii. Et nam voluptua appetere.</p>
    <p>Ex inani argumentum appellantur nam, noster graeco vel ei, et quod agam posse per. Has cu quot fastidii dissentiet. Ei cum duis fastidii. Et nam voluptua appetere, cu eos graeco facilis philosophia. Mei appetere forensibus at, timeam facilisis eu quo. Ei cum duis fastidii. Et nam voluptua appetere, cu eos graeco facilis philosophia.</p>
  </section>
</main>
</body>
</html>
```